Doctors Office Web Design

Name of the business is Lian-Hua Qiu M.D.
We need a web design that is attractive for women that want to see Dr. Lian-Hua Qiu for Obstetrician Gynecology and Pregnancy care. Dr. Qiu earned her degree from Harbor Crest Medical College of obstetrician gynecology. We want to attract women of child bearing ages to come to our offices for health, education, and pregnancies.

Please visit http://www.drqiucare-example.com/ to help you get a feel for who we are. We will be adding some pictures and logo in the next few days.

We are looking for to have pages for and tabs including
About Us- History, Our Staff, Dr. Qiu
Patient Information- Appointments, E-Prescriptions, Payments Accepted, Insurance
Health- General, Sexual, Mental, Affiliates
Pregnancy- Minimally invasive surgery(our specialty), 4-D Ultra Sound, Hospital Affiliations
Media- News,Pictures, Videos
Locations- Palmvale Office, Marlow Office

The colors we would like to use are pastel colors, magenta, and plum

Target Market(s)

Women of all ages with an emphasis on 25-65 year olds

Industry/Entity Type

Business

Requirements
Must have
• Needs to include a location for a our videos and pictures that I will submit shortly. We also want a map to our location or atleast a place for one.
Nice to have
• A place for a google map of our office locations.

```html
<!DOCTYPE html>
<html lang="en">
<head>
<meta charset="utf-8">
<title>Dr. Lian-Hua Qiu M.D.</title>
<link href="https://fonts.googleapis.com/css2?family=Alfa+Slab+One&family=Kotta+One&family=Ubuntu:wght@400;500&display=swap" rel="stylesheet">
<style>
  :root {
    --plum: #7e1140;
    --plum-dark: #6e0f37;
    --tab: #851445;
    --mauve-text: #7d3b58;
    --header-top: #d4bfc9;
    --header-bottom: #eee3e8;
    --rule: #b9b3b6;
    --wine-text: #7a1a3e;
    --ribbon: #9a6b7f;
    --white: #ffffff;
    --panel-grey: #f1eeef;
  }
  * { margin: 0; padding: 0; box-sizing: border-box; }
  html, body { width: 1200px; height: 1080px; overflow: hidden; background: var(--white); }
  .page { position: relative; width: 1200px; height: 1080px; overflow: hidden; background: var(--white); }

  .site-header {
    position: absolute; left: 0; top: 0; width: 1200px; height: 182px;
    background: linear-gradient(180deg, var(--header-top) 0%, var(--header-bottom) 100%);
    border-top: 10px solid var(--plum-dark);
  }
  .header-rule { position: absolute; left: 0; top: 182px; width: 1200px; height: 4px; background: var(--rule); }

  .main-nav { position: absolute; left: 263px; top: 0; display: flex; gap: 2px; }
  .main-nav a {
    display: block; width: 145px; height: 48px; line-height: 44px;
    background: var(--tab); color: var(--white); text-decoration: none; text-align: center;
    font-family: "Ubuntu", sans-serif; font-size: 19px; letter-spacing: 0.5px;
    border-radius: 0 0 5px 5px;
  }
  .main-nav a.wide { margin-left: 0; }

  .brand { position: absolute; left: 85px; top: 112px; color: var(--mauve-text); font-family: "Ubuntu", sans-serif; }
  .brand-name { font-size: 37px; font-weight: 400; line-height: 1; }
  .brand-name small { font-size: 17px; margin-left: 8px; vertical-align: 10px; }
  .brand-tagline { font-size: 17px; font-weight: 500; margin-top: 4px; }

  .welcome { position: absolute; left: 101px; top: 230px; width: 660px; font-family: "Kotta One", serif; color: var(--wine-text); }
  .welcome h1 { font-size: 22px; font-weight: 400; margin-bottom: 6px; }
  .welcome p { font-size: 16.5px; line-height: 34px; }
  .welcome strong { font-weight: 700; }

  .doctor-photo {
    position: absolute; left: 834px; top: 220px; width: 307px; height: 461px;
    background: linear-gradient(180deg, #f5f3f2 0%, #e3e8ee 55%, #cfd7e0 100%);
  }

  .specialties {
    position: absolute; left: 98px; top: 458px; width: 661px; height: 222px;
    background: linear-gradient(90deg, #ece6e4 0%, #f7f5f5 60%, var(--white) 100%);
    border: 1px solid #c9c3c5; box-shadow: 3px 3px 2px #55474d;
  }
  .specialties-photo {
    position: absolute; left: 0; top: 0; width: 148px; height: 100%;
    background: linear-gradient(180deg, #e6dcd5 0%, #f2ece8 50%, #e9e1dc 100%);
  }
  .specialties-text {
    position: absolute; left: 198px; top: 38px; width: 420px;
    font-family: "Kotta One", serif; font-size: 20.5px; line-height: 34px; color: var(--wine-text); font-weight: 700;
  }

  .site-footer { position: absolute; left: 0; top: 724px; width: 1200px; height: 356px; background: var(--plum); }
  .zigzag { position: absolute; left: 0; top: -8px; }

  .ribbon { position: absolute; width: 62px; height: 104px; }
  .ribbon-contact { left: 98px; top: 708px; }
  .ribbon-videos { left: 708px; top: 712px; }

  .section-title {
    position: absolute; font-family: "Alfa Slab One", serif; color: var(--white);
    font-size: 20px; letter-spacing: 3px; font-weight: 400;
  }
  .title-contact { left: 169px; top: 771px; }
  .title-videos { left: 785px; top: 771px; }

  .map-frame {
    position: absolute; left: 101px; top: 854px; width: 169px; height: 158px;
    border: 3px solid #9c8f96; background: linear-gradient(135deg, #f4f6fb 0%, #dfe6f2 100%);
  }

  .address { position: absolute; left: 299px; top: 870px; font-family: "Ubuntu", sans-serif; font-size: 19px; line-height: 29px; color: var(--white); font-style: normal; }

  .video-player { position: absolute; left: 786px; top: 817px; width: 282px; height: 234px; background: #000; }
  .video-controls { position: absolute; left: 0; bottom: 0; width: 100%; height: 17px; background: #d9d9d9; border-top: 1px solid #9a9a9a; }
  .play-button { position: absolute; left: 118px; top: 93px; }
</style>
</head>
<body>
<div class="page">

  <header class="site-header">
    <nav class="main-nav">
      <a href="#">ABOUT US</a>
      <a href="#">PATIENT INFO</a>
      <a href="#">HEALTH</a>
      <a href="#">PREGNANCY</a>
      <a href="#">MEDIA</a>
      <a href="#">LOCATIONS</a>
    </nav>
    <div class="brand">
      <div class="brand-name">Dr. Lian-Hua Qiu<small>m.d.,</small></div>
      <div class="brand-tagline">facog board certified&nbsp; Obstetrician/Gynecologist</div>
    </div>
  </header>
  <div class="header-rule"></div>

  <section class="welcome">
    <h1>Welcome to Dr. Lian-Hua Qiu's website.</h1>
    <p>Here you will be able to find information about both of our offices, meet Dr. Qiu and her staff, and browse through our women's health links to learn more about pregnancy, nutrition, exercise, and other women's health issues. Serving Have fun and if you have any questions, feel free to contact us at <strong>drqiu@harborline-example.net</strong></p>
  </section>

  <div class="doctor-photo" role="img" aria-label="Photo of a smiling doctor in a white coat holding a folder"></div>

  <section class="specialties">
    <div class="specialties-photo" role="img" aria-label="Photo of an expectant mother seated in white"></div>
    <p class="specialties-text">All Areas of Women's Health, including: Obstetrics, Family Planning, Hormonal Evaluation, Incontinence, Infertility, and Gynecology Surgery</p>
  </section>

  <footer class="site-footer">
    <svg class="zigzag" width="1200" height="9" viewBox="0 0 1200 9" aria-hidden="true">
      <polygon fill="#7e1140" points="0,9 0,3 5,0 10,3 15,0 20,3 25,0 30,3 35,0 40,3 45,0 50,3 55,0 60,3 65,0 70,3 75,0 80,3 85,0 90,3 95,0 100,3 105,0 110,3 115,0 120,3 125,0 130,3 135,0 140,3 145,0 150,3 155,0 160,3 165,0 170,3 175,0 180,3 185,0 190,3 195,0 200,3 205,0 210,3 215,0 220,3 225,0 230,3 235,0 240,3 245,0 250,3 255,0 260,3 265,0 270,3 275,0 280,3 285,0 290,3 295,0 300,3 305,0 310,3 315,0 320,3 325,0 330,3 335,0 340,3 345,0 350,3 355,0 360,3 365,0 370,3 375,0 380,3 385,0 390,3 395,0 400,3 405,0 410,3 415,0 420,3 425,0 430,3 435,0 440,3 445,0 450,3 455,0 460,3 465,0 470,3 475,0 480,3 485,0 490,3 495,0 500,3 505,0 510,3 515,0 520,3 525,0 530,3 535,0 540,3 545,0 550,3 555,0 560,3 565,0 570,3 575,0 580,3 585,0 590,3 595,0 600,3 605,0 610,3 615,0 620,3 625,0 630,3 635,0 640,3 645,0 650,3 655,0 660,3 665,0 670,3 675,0 680,3 685,0 690,3 695,0 700,3 705,0 710,3 715,0 720,3 725,0 730,3 735,0 740,3 745,0 750,3 755,0 760,3 765,0 770,3 775,0 780,3 785,0 790,3 795,0 800,3 805,0 810,3 815,0 820,3 825,0 830,3 835,0 840,3 845,0 850,3 855,0 860,3 865,0 870,3 875,0 880,3 885,0 890,3 895,0 900,3 905,0 910,3 915,0 920,3 925,0 930,3 935,0 940,3 945,0 950,3 955,0 960,3 965,0 970,3 975,0 980,3 985,0 990,3 995,0 1000,3 1005,0 1010,3 1015,0 1020,3 1025,0 1030,3 1035,0 1040,3 1045,0 1050,3 1055,0 1060,3 1065,0 1070,3 1075,0 1080,3 1085,0 1090,3 1095,0 1100,3 1105,0 1110,3 1115,0 1120,3 1125,0 1130,3 1135,0 1140,3 1145,0 1150,3 1155,0 1160,3 1165,0 1170,3 1175,0 1180,3 1185,0 1190,3 1195,0 1200,3 1200,9"/>
    </svg>
  </footer>

  <svg class="ribbon ribbon-contact" viewBox="0 0 62 104" aria-hidden="true">
    <polygon fill="#9a6b7f" points="0,0 62,0 62,104 31,76 0,104"/>
  </svg>
  <h2 class="section-title title-contact">CONTACT US &amp; LOCATION</h2>

  <svg class="ribbon ribbon-videos" viewBox="0 0 62 104" aria-hidden="true">
    <polygon fill="#9a6b7f" points="0,0 62,0 62,104 31,76 0,104"/>
  </svg>
  <h2 class="section-title title-videos">OUR VIDEOS</h2>

  <div class="map-frame" role="img" aria-label="Street map showing the route to the office"></div>

  <address class="address">
    4410 Lantern Grove Avenue<br>
    Suite 210-212<br>
    Marlow, Florida&nbsp; 33999<br>
    Tel:&nbsp; (555) 014-2288<br>
    Fax: (555) 014-2290
  </address>

  <div class="video-player">
    <svg class="play-button" width="46" height="32" viewBox="0 0 46 32" aria-hidden="true">
      <rect x="1" y="1" width="44" height="30" rx="5" fill="#8c8c8c" stroke="#bdbdbd"/>
      <polygon points="18,9 18,23 29,16" fill="#ededed"/>
    </svg>
    <div class="video-controls">
      <svg width="282" height="16" viewBox="0 0 282 16" aria-hidden="true">
        <polygon points="6,4 6,12 12,8" fill="#333"/>
        <rect x="22" y="6" width="170" height="4" rx="2" fill="#a5a5a5"/>
        <circle cx="25" cy="8" r="4" fill="#666"/>
        <rect x="204" y="4" width="40" height="8" fill="#c9c9c9"/>
        <rect x="262" y="4" width="12" height="8" rx="2" fill="#333"/>
      </svg>
    </div>
  </div>

</div>
</body>
</html>
```